Medical Oncologist in Rural Australia needs a Business Card

I am a medical oncologist in a regional town in Australia. I need a business card that merges a degree of conservatism (as people's lives are entrusted to me) with cutting edge (as I am always trying to understand the latest cancer biology and trying to bring new drugs to patients rapidly). I wish my card to project the idea that I am trustworthy, caring and innovative. Not overly bold colours but something that doesn't drift into the background.

Medical

```html
<!DOCTYPE html>
<html lang="en">
<head>
<meta charset="UTF-8">
<title>Riverbend Medical Oncology – Business Card</title>
<link href="https://fonts.googleapis.com/css2?family=Exo+2:wght@300;400;500;600&display=swap" rel="stylesheet">
<style>
  :root {
    --backdrop: #7af4f2;
    --brand-blue: #0a78a6;
    --brand-blue-light: #1a8fbd;
    --ink-black: #050505;
    --paper-white: #ffffff;
    --muted-white: #e8e8e8;
  }
  * { margin: 0; padding: 0; box-sizing: border-box; }
  html, body {
    width: 1200px;
    height: 900px;
    overflow: hidden;
    background: var(--backdrop);
    font-family: "Exo 2", "Trebuchet MS", sans-serif;
  }
  .canvas {
    position: relative;
    width: 1200px;
    height: 900px;
  }
  .card {
    position: absolute;
    width: 560px;
    height: 320px;
    left: 320px;
    border-radius: 4px;
    overflow: hidden;
    box-shadow: 0 10px 24px rgba(0, 40, 50, 0.25);
  }
  .card-front {
    top: 100px;
    background: var(--ink-black);
  }
  .front-panel {
    position: absolute;
    inset: 18px;
    background: linear-gradient(135deg, var(--brand-blue-light), var(--brand-blue) 60%);
    display: flex;
    align-items: center;
    justify-content: center;
    gap: 16px;
  }
  .brand-dot {
    width: 46px;
    height: 46px;
    border-radius: 50%;
    border: 3px solid var(--paper-white);
    flex: none;
  }
  .brand-name {
    font-weight: 500;
    letter-spacing: 1px;
    text-transform: uppercase;
  }
  .front-panel .brand-name {
    color: var(--paper-white);
    font-size: 24px;
  }

  .card-back {
    top: 480px;
    background: var(--ink-black);
  }
  .back-shapes {
    position: absolute;
    inset: 0;
  }
  .back-brand {
    position: absolute;
    top: 34px;
    left: 40px;
    display: flex;
    align-items: center;
    gap: 14px;
  }
  .back-brand .brand-dot {
    width: 36px;
    height: 36px;
    border-color: var(--brand-blue);
  }
  .back-brand .brand-name {
    color: var(--ink-black);
    font-size: 21px;
    font-weight: 600;
  }
  .person {
    position: absolute;
    left: 30px;
    top: 168px;
    color: var(--paper-white);
  }
  .person-name {
    font-size: 20px;
    font-weight: 500;
  }
  .person-credentials {
    font-size: 12.5px;
    font-weight: 300;
    color: var(--muted-white);
    margin-top: 2px;
  }
  .address {
    position: absolute;
    left: 30px;
    top: 240px;
  }
  .contact-list {
    position: absolute;
    right: 26px;
    bottom: 22px;
    list-style: none;
    text-align: right;
  }
  .contact-line {
    display: flex;
    align-items: center;
    justify-content: flex-end;
    gap: 7px;
    color: var(--muted-white);
    font-size: 12.5px;
    font-weight: 300;
    line-height: 20px;
  }
  .address.contact-line { justify-content: flex-start; }
  .contact-icon {
    width: 12px;
    height: 12px;
    flex: none;
  }
</style>
</head>
<body>
<main class="canvas">

  <section class="card card-front" aria-label="Business card front">
    <div class="front-panel">
      <span class="brand-dot" aria-hidden="true"></span>
      <span class="brand-name">Riverbend Medical Oncology</span>
    </div>
  </section>

  <section class="card card-back" aria-label="Business card back">
    <svg class="back-shapes" viewBox="0 0 560 320" width="560" height="320" aria-hidden="true">
      <polygon points="0,0 560,0 560,112 0,140" fill="var(--paper-white)"/>
      <polygon points="0,140 560,112 560,136 0,164" fill="var(--brand-blue)"/>
    </svg>

    <div class="back-brand">
      <span class="brand-dot" aria-hidden="true"></span>
      <span class="brand-name">Riverbend Medical Oncology</span>
    </div>

    <div class="person">
      <p class="person-name">Jane Doe</p>
      <p class="person-credentials">MBBS (hons), FRACP, BE (hons)</p>
    </div>

    <p class="address contact-line">
      <svg class="contact-icon" viewBox="0 0 12 12"><circle cx="6" cy="6" r="6" fill="var(--paper-white)"/><path d="M6 2.5a2 2 0 0 0-2 2c0 1.6 2 4.5 2 4.5s2-2.9 2-4.5a2 2 0 0 0-2-2z" fill="var(--ink-black)"/></svg>
      Building, Street No., City, State, Zipcode
    </p>

    <ul class="contact-list">
      <li class="contact-line">+123 456 7890
        <svg class="contact-icon" viewBox="0 0 12 12"><circle cx="6" cy="6" r="6" fill="var(--paper-white)"/><path d="M3.6 3.2l1.2-.4.7 1.5-.7.6a4 4 0 0 0 1.9 1.9l.6-.7 1.5.7-.4 1.2c-2.6.2-5-2.2-4.8-4.8z" fill="var(--ink-black)"/></svg>
      </li>
      <li class="contact-line">janedoe@email.com
        <svg class="contact-icon" viewBox="0 0 12 12"><circle cx="6" cy="6" r="6" fill="var(--paper-white)"/><rect x="3" y="4" width="6" height="4.2" fill="none" stroke="var(--ink-black)" stroke-width="0.9"/><path d="M3 4l3 2.3L9 4" fill="none" stroke="var(--ink-black)" stroke-width="0.9"/></svg>
      </li>
      <li class="contact-line">www.web.com
        <svg class="contact-icon" viewBox="0 0 12 12"><circle cx="6" cy="6" r="6" fill="var(--paper-white)"/><circle cx="6" cy="6" r="3" fill="none" stroke="var(--ink-black)" stroke-width="0.9"/><path d="M3 6h6M6 3c-1.2 1.6-1.2 4.4 0 6M6 3c1.2 1.6 1.2 4.4 0 6" fill="none" stroke="var(--ink-black)" stroke-width="0.7"/></svg>
      </li>
    </ul>
  </section>

</main>
</body>
</html>
```